Fence & Deck Construction Flyer

My company is called Brackley Fence & Deck and I am seeking a flyer for direct marketing our construction services to residential customers in Calgary. Our focus is home owners aged 35+ that are looking to replace an old fence or deck, although we also do new construction. We use pressure treated wood mainly, but we also use cedar and composite products. You can view our website at www.brackleyfence.ca for some additional insight and pictures of our previous projects. Company colors are black and deep yellow (see website).
The size of the flyer will need to be 6 inches by 11 inches, both sides in full colour.

```html
<!DOCTYPE html>
<html lang="en">
<head>
<meta charset="utf-8">
<title>Brackley Fence &amp; Deck – Flyer</title>
<link rel="stylesheet" href="https://fonts.googleapis.com/css2?family=Audiowide&family=Yanone+Kaffeesatz:wght@400;500;700&family=Open+Sans:wght@700&display=swap">
<style>
  :root {
    --orange: #f7901e;
    --orange-deep: #c85f0a;
    --black: #141414;
    --wood-dark: #1c1c1c;
    --wood-mid: #2e2e2e;
    --band: #3a3a3a;
    --white: #ffffff;
    --page: #f2f2f2;
  }
  * { box-sizing: border-box; margin: 0; padding: 0; }
  html, body { width: 927px; height: 1200px; overflow: hidden; background: var(--page); }
  .canvas { position: relative; width: 927px; height: 1200px; }

  .flyer {
    position: absolute; top: 276px; width: 360px; height: 647px;
    background: radial-gradient(ellipse at center, var(--black) 55%, var(--orange-deep) 100%);
    box-shadow: 0 4px 14px rgba(0,0,0,.35);
  }
  .flyer--front { left: 94px; }
  .flyer--back { left: 473px; }
  .flyer__body {
    position: absolute; inset: 10px;
    background: linear-gradient(90deg, var(--wood-dark), var(--wood-mid) 30%, var(--wood-dark) 55%, var(--wood-mid) 80%, var(--wood-dark));
  }
  .flyer__frame {
    position: absolute; inset: 18px; border: 2px solid var(--orange-deep); z-index: 3; pointer-events: none;
  }
  .abs { position: absolute; left: 0; right: 0; text-align: center; z-index: 2; white-space: nowrap; }

  .company-name {
    font-family: "Yanone Kaffeesatz", sans-serif; font-weight: 700;
    color: var(--orange); font-size: 40px; line-height: 1;
  }

  .tagline { font-family: "Yanone Kaffeesatz", sans-serif; font-weight: 400; color: var(--white); font-size: 24px; }
  .phone { font-family: "Audiowide", sans-serif; font-size: 27px; letter-spacing: 1px; }
  .phone--orange { color: var(--orange); }
  .phone--white { color: var(--white); }

  .headline { font-family: "Audiowide", sans-serif; color: var(--white); line-height: 1; }
  .headline--big { font-size: 34px; }
  .headline--small { font-size: 28px; }

  .offer-band {
    position: absolute; left: 10px; right: 10px; z-index: 1;
    background: linear-gradient(180deg, var(--band), #262626);
  }
  .offer-band--front { top: 365px; bottom: 10px; }
  .offer-band--back { top: 461px; height: 132px; }

  .ribbon { position: absolute; top: 372px; z-index: 2; }
  .ribbon text { font-family: "Yanone Kaffeesatz", sans-serif; fill: var(--black); }

  .material { position: absolute; top: 465px; width: 92px; z-index: 2; }
  .material__frame {
    height: 74px; border-radius: 9px; background: var(--black);
    border: 3px solid var(--orange); overflow: hidden;
  }
  .material__label {
    font-family: "Yanone Kaffeesatz", sans-serif; font-size: 12px; color: var(--white);
    text-align: center; height: 18px; line-height: 18px; background: #111; white-space: nowrap; overflow: hidden;
  }
  .material__sample { height: 50px; }
  .material__sample--spruce { background: linear-gradient(160deg, #e8c89a, #b88a55); }
  .material__sample--cedar { background: linear-gradient(160deg, #e4a574, #a85a32); }
  .material__sample--composite { background: linear-gradient(160deg, #d2b293, #8e6c52); }

  .price { position: relative; width: 80px; height: 80px; margin: -10px auto 0; }
  .price svg { position: absolute; inset: 0; }
  .price__text {
    position: absolute; inset: 0; display: flex; flex-direction: column; align-items: center; justify-content: center;
    font-family: "Yanone Kaffeesatz", sans-serif; color: var(--white); line-height: 1;
  }
  .price__from { font-size: 13px; }
  .price__value { font-size: 30px; font-weight: 700; }
  .price__value small { font-size: 12px; font-weight: 400; }

  .project-grid {
    position: absolute; top: 213px; left: 50px; width: 260px; z-index: 2;
    display: grid; grid-template-columns: 122px 122px; gap: 8px 14px;
  }
  .project-photo {
    height: 107px; border-radius: 10px; border: 3px solid var(--orange);
    background: linear-gradient(180deg, #b9b3bd 0%, #a69a88 45%, #8a7556 70%, #6e6550 100%);
  }

  .cta { font-family: "Open Sans", sans-serif; font-weight: 700; color: var(--white); font-size: 17px; line-height: 27px; }
  .website { font-family: "Audiowide", sans-serif; color: var(--orange); font-size: 18px; letter-spacing: 1px; }
</style>
</head>
<body>
<div class="canvas">

  <section class="flyer flyer--front">
    <div class="flyer__body"></div>
    <div class="offer-band offer-band--front"></div>
    <div class="flyer__frame"></div>

    <div class="abs company-name" style="top:118px;">Brackley Fence &amp; Deck</div>
    <div class="abs tagline" style="top:190px;">“ the residential specialists ”</div>
    <div class="abs phone phone--orange" style="top:228px;">403-5550182</div>
    <div class="abs headline headline--big" style="top:290px;">REPLACE</div>
    <div class="abs headline headline--small" style="top:328px;">YOUR DECK</div>

    <svg class="ribbon" style="left:22px;" width="160" height="80" viewBox="0 0 160 80">
      <polygon points="0,46 22,18 150,8 146,62 22,70" fill="#f7901e"/>
      <polygon points="130,4 150,8 146,16" fill="#a94c05"/>
      <text x="24" y="58" font-size="36" font-weight="700" transform="rotate(-6 24 58)">FREE</text>
      <text x="84" y="30" font-size="13" transform="rotate(-6 84 30)">on-site</text>
      <text x="84" y="43" font-size="13" transform="rotate(-6 84 43)">consultation</text>
      <text x="84" y="56" font-size="13" transform="rotate(-6 84 56)">&amp; quote!</text>
    </svg>
    <svg class="ribbon" style="left:176px;" width="164" height="80" viewBox="0 0 164 80">
      <polygon points="0,40 26,6 158,14 152,70 18,74" fill="#f7901e"/>
      <polygon points="140,4 158,14 150,18" fill="#a94c05"/>
      <text x="26" y="28" font-size="17" transform="rotate(6 26 28)">SAVE</text>
      <text x="22" y="60" font-size="32" font-weight="700" transform="rotate(6 22 60)">$50</text>
      <text x="76" y="36" font-size="13" transform="rotate(6 76 36)">on removal</text>
      <text x="74" y="50" font-size="13" transform="rotate(6 74 50)">&amp; haul away</text>
      <text x="72" y="64" font-size="13" transform="rotate(6 72 64)">of your deck</text>
    </svg>

    <div class="material" style="left:28px;">
      <div class="material__frame">
        <div class="material__label">pressure treated spruce</div>
        <div class="material__sample material__sample--spruce" role="img" aria-label="Pressure treated spruce boards"></div>
      </div>
      <div class="price">
        <svg viewBox="0 0 80 80"><g fill="#f7901e"><circle cx="40" cy="40" r="30"/><circle cx="70" cy="40" r="8"/><circle cx="66" cy="55" r="8"/><circle cx="55" cy="66" r="8"/><circle cx="40" cy="70" r="8"/><circle cx="25" cy="66" r="8"/><circle cx="14" cy="55" r="8"/><circle cx="10" cy="40" r="8"/><circle cx="14" cy="25" r="8"/><circle cx="25" cy="14" r="8"/><circle cx="40" cy="10" r="8"/><circle cx="55" cy="14" r="8"/><circle cx="66" cy="25" r="8"/></g></svg>
        <div class="price__text"><span class="price__from">starting from</span><span class="price__value">$12<small>/sq.ft.</small></span></div>
      </div>
    </div>
    <div class="material" style="left:134px;">
      <div class="material__frame">
        <div class="material__label">western red color</div>
        <div class="material__sample material__sample--cedar" role="img" aria-label="Western red cedar boards"></div>
      </div>
      <div class="price">
        <svg viewBox="0 0 80 80"><g fill="#f7901e"><circle cx="40" cy="40" r="30"/><circle cx="70" cy="40" r="8"/><circle cx="66" cy="55" r="8"/><circle cx="55" cy="66" r="8"/><circle cx="40" cy="70" r="8"/><circle cx="25" cy="66" r="8"/><circle cx="14" cy="55" r="8"/><circle cx="10" cy="40" r="8"/><circle cx="14" cy="25" r="8"/><circle cx="25" cy="14" r="8"/><circle cx="40" cy="10" r="8"/><circle cx="55" cy="14" r="8"/><circle cx="66" cy="25" r="8"/></g></svg>
        <div class="price__text"><span class="price__from">starting from</span><span class="price__value">$15<small>/sq.ft.</small></span></div>
      </div>
    </div>
    <div class="material" style="left:240px;">
      <div class="material__frame">
        <div class="material__label">composite decking</div>
        <div class="material__sample material__sample--composite" role="img" aria-label="Composite decking boards"></div>
      </div>
      <div class="price">
        <svg viewBox="0 0 80 80"><g fill="#f7901e"><circle cx="40" cy="40" r="30"/><circle cx="70" cy="40" r="8"/><circle cx="66" cy="55" r="8"/><circle cx="55" cy="66" r="8"/><circle cx="40" cy="70" r="8"/><circle cx="25" cy="66" r="8"/><circle cx="14" cy="55" r="8"/><circle cx="10" cy="40" r="8"/><circle cx="14" cy="25" r="8"/><circle cx="25" cy="14" r="8"/><circle cx="40" cy="10" r="8"/><circle cx="55" cy="14" r="8"/><circle cx="66" cy="25" r="8"/></g></svg>
        <div class="price__text"><span class="price__from">starting from</span><span class="price__value">$22<small>/sq.ft.</small></span></div>
      </div>
    </div>
  </section>

  <section class="flyer flyer--back">
    <div class="flyer__body"></div>
    <div class="offer-band offer-band--back"></div>
    <div class="flyer__frame"></div>

    <div class="abs company-name" style="top:96px;">Brackley Fence &amp; Deck</div>
    <div class="abs tagline" style="top:160px;">“ the residential specialists ”</div>

    <div class="project-grid">
      <div class="project-photo" role="img" aria-label="Finished backyard deck with privacy screen"></div>
      <div class="project-photo" role="img" aria-label="New wooden deck with horizontal slat fence"></div>
      <div class="project-photo" role="img" aria-label="Low platform deck behind a house"></div>
      <div class="project-photo" role="img" aria-label="Deck with slatted privacy wall under blue sky"></div>
    </div>

    <div class="abs cta" style="top:468px;">call or go online to request<br>a FREE on site quote</div>
    <div class="abs website" style="top:540px;">WWW.BRACKLEYFENCE.CA</div>
    <div class="abs phone phone--white" style="top:566px;">403-555-0182</div>
  </section>

</div>
</body>
</html>
```